Flyer Design for new yoga and pilates studio for Health care centre

We are a health care company in Sydney CBD, we have chiropractors, podiatry, massage, nutrition, massage etc. but we are now expanding to add Yoga and Pilates to our centre.
We want to make sure the emphasis that that studio will be boutique, never crowded, limited number of participants and run by health professionals. Also that is it located in the Sydney CBD opposite MRH. Our target is more corporate since we are in the City. This flyer will be handed out in the street in the city to inform people of our new studio. The flyer must be A5 and include our logo and our colours which I have attached. Our website is www.harbourvitalclinic.com.au.
Thank you!

Requirements
Must have
• the flyer must be A5 in size and include our logo, our colours and you can use one or more of the photos provided. I have attached the photos.

```html
<!DOCTYPE html>
<html lang="en">
<head>
<meta charset="utf-8">
<title>Yoga &amp; Pilates Studio – Harbour Vital Clinic</title>
<link rel="stylesheet" href="https://fonts.googleapis.com/css2?family=Inter:wght@300;400;600;700;800&display=swap">
<style>
  :root {
    --backdrop: #4a4344;
    --magenta: #b81e81;
    --amber: #e38f2a;
    --violet: #6461ae;
    --paper: #ffffff;
    --ink: #1d1b1c;
    --band-dark: #2a2526;
    --warm: #ee9950;
    --heading-violet: #3535a0;
    --panel: rgba(255, 255, 255, 0.38);
  }
  * { box-sizing: border-box; margin: 0; padding: 0; }
  html, body { width: 924px; height: 1200px; overflow: hidden; }
  body { background: var(--backdrop); font-family: "Inter", Arial, sans-serif; color: var(--ink); }

  .flyer {
    position: absolute; left: 77px; top: 5px;
    width: 770px; height: 1190px;
    background: var(--warm);
    box-shadow: 0 2px 8px rgba(0,0,0,.35);
    overflow: hidden;
  }
  .colour-stripe { position: absolute; top: 0; left: 0; width: 770px; height: 37px; display: flex; }
  .colour-stripe .magenta { width: 370px; background: var(--magenta); }
  .colour-stripe .amber { width: 92px; background: var(--amber); }
  .colour-stripe .violet { flex: 1; background: var(--violet); }

  .hero { position: absolute; top: 37px; left: 0; width: 770px; height: 520px; background: var(--paper); }
  .hero-photo { position: absolute; left: 0; top: 0; }
  .headline { position: absolute; left: 0; top: 0; font-weight: 300; color: var(--ink); line-height: 1; }
  .headline span { position: absolute; white-space: nowrap; letter-spacing: -2px; }
  .headline .new { left: 130px; top: 48px; font-size: 56px; letter-spacing: -1px; }
  .headline .yoga { left: 80px; top: 85px; font-size: 122px; }
  .headline .amp { left: 374px; top: 130px; font-size: 80px; }
  .headline .pilates { left: 86px; top: 200px; font-size: 122px; }
  .headline .studio { left: 133px; top: 315px; font-size: 56px; letter-spacing: -1px; }

  .venue-band {
    position: absolute; top: 557px; left: 0; width: 770px; height: 60px;
    background: var(--band-dark); color: #fff;
    font-size: 29px; font-weight: 700; text-align: center; line-height: 60px;
  }

  .intro {
    position: absolute; left: 86px; top: 636px; width: 598px;
    font-size: 17.5px; line-height: 25.5px; text-align: justify; font-weight: 400;
  }
  .benefits { position: absolute; left: 86px; top: 745px; list-style: none; font-size: 18px; font-weight: 600; }
  .benefits li { height: 31px; }
  .benefits li::before { content: "• "; }

  .services-panel {
    position: absolute; left: 46px; top: 850px; width: 678px; height: 107px;
    background: var(--panel); text-align: center;
  }
  .services-panel h2 { margin-top: 8px; font-size: 25px; font-weight: 700; color: var(--heading-violet); }
  .services-panel p { font-size: 18px; font-weight: 600; line-height: 25px; }
  .services-panel p:first-of-type { margin-top: 6px; }

  .call-line { position: absolute; left: 43px; top: 969px; font-size: 18px; font-weight: 600; white-space: nowrap; }
  .call-line strong { font-weight: 800; letter-spacing: 1px; }

  .brand-band {
    position: absolute; top: 1003px; left: 0; width: 770px; height: 75px;
    background: var(--magenta);
    display: flex; align-items: center; justify-content: center;
  }
  .brand-name { color: #fff; font-size: 40px; font-weight: 700; letter-spacing: -0.5px; }

  .address { position: absolute; left: 185px; top: 1089px; font-size: 18px; line-height: 25.5px; font-weight: 400; }
</style>
</head>
<body>
  <main class="flyer">
    <div class="colour-stripe"><div class="magenta"></div><div class="amber"></div><div class="violet"></div></div>

    <section class="hero">
      <svg class="hero-photo" width="770" height="520" viewBox="0 0 770 520" role="img" aria-label="Photo of a woman in an upward-facing dog yoga pose on a mat">
        <defs>
          <linearGradient id="poseTone" x1="0" y1="0" x2="1" y2="1">
            <stop offset="0" stop-color="#ffffff"/>
            <stop offset="0.6" stop-color="#f1e4da"/>
            <stop offset="1" stop-color="#d9c2b2"/>
          </linearGradient>
          <linearGradient id="matTone" x1="0" y1="0" x2="0" y2="1">
            <stop offset="0" stop-color="#c9cec4"/>
            <stop offset="1" stop-color="#8f9a8c"/>
          </linearGradient>
        </defs>
        <rect x="300" y="60" width="470" height="440" fill="url(#poseTone)"/>
        <rect x="0" y="500" width="770" height="20" fill="url(#matTone)"/>
      </svg>
      <h1 class="headline">
        <span class="new">New</span>
        <span class="yoga">yoga</span>
        <span class="amp">&amp;</span>
        <span class="pilates">pilates</span>
        <span class="studio">Studio</span>
      </h1>
    </section>

    <div class="venue-band">now at Harbour Vital Clinic</div>

    <p class="intro">Harbour Vital Clinic is opening our brand new Yoga &amp; Pilates studio. Our point of difference is our classes are overseen by Health professionals to ensure you get maximum results with no injuries.</p>

    <ul class="benefits">
      <li>Unique approach to fitness and health</li>
      <li>Limit clients per class, best instructors in Sydney</li>
      <li>Located in the Sydney CBD, opposite the MRH</li>
    </ul>

    <section class="services-panel">
      <h2>Harbour Vital Clinic - For complete wellbeing</h2>
      <p>• Chiropractic • Podiatry • Nutrition • Massage • Acupuncture</p>
      <p>• Yoga • Pilates • Backcare &amp; Scoliosis classes</p>
    </section>

    <p class="call-line">Call now for opening specials - <strong>Limited place -&nbsp; P: 9411 2750</strong></p>

    <div class="brand-band"><span class="brand-name">Harbour Vital Clinic</span></div>

    <address class="address" style="font-style:normal">
      Level 5, Lantern House, 48 Pitt St<br>
      (Opposite the MRH) Sydney NSW 2000 Australia<br>
      Tel: (02) 9411 2750 Fax: (02) 9411 2793
    </address>
  </main>
</body>
</html>
```